BRONVEL FOOD: Window / Poster Advertising

Bronvel is a store providing great, ready-to-eat, no-fuss food. Our main items are Pita meals, and Super Salads. And we have a need to advertise this food on the go business!

We have a large number of pedestrians passing the store three times per day, and require some advertising to promote or food, and attract these people. We are looking to have artwork created for use within the window and A-Frame. Effectively, a Poster Design. The size required is A1 (594mm x 841mm).

Common terms we use within the store and with our customers are:
- "Fine Food Take Out On The Go"
- "In and Out"
- "A Meal in a Pita"
These could be a source of promotion within the artwork

To keep a consistent branding, the "BRONVEL" text/font, and Blue Owl image must be used (attached). Fonts: bronvel font is called "goodmorningafternoon" and the font used for dine the wide-world style is called "whipsmart" both of which can be downloaded for free. You can view our Chatterly page here www.chatterly.example/bronvelfood however, we are very open to the introduction of new colour and imagery. We are fond of the current Quikmart advertising which has a slightly animated effect - example attached.
Updates

Hi all 

we have uploaded a few pictures which we would love you to draw some inspiration from. It is the design that is featured on most frostee cups and frostee machines in all Quikmarts. We really like this pop of colour and animated yet modernized look. We realised that although advertising the food is a great way to show the customer what we have we want a more generalised eye catching sort of advertisment that can be featured on our window no matter what the food we are serving. We are a very innovative shop that is constantly updating our menu and therefore we dont want one thing to be featured amongst the others. Please draw inspiration from the images uploaded aswell as from our chatterly page (www.chatterly.example/bronvelfood) to come up with something amazing!! were really loving the creativity and hope that these few images will help you understand exactly what we want. 

Warm Regards 

Industry/Entity Type

Advertising

```html
<!DOCTYPE html>
<html lang="en">
<head>
<meta charset="utf-8">
<title>Bronvel – Dine the wide-world style</title>
<link rel="stylesheet" href="https://fonts.googleapis.com/css2?family=Poppins:wght@500;800&display=swap">
<style>
  :root {
    --sky: #1fa4c8;
    --ray: #4fc0dc;
    --band: #fff200;
    --ink: #111111;
    --mark: #25a83a;
  }
  html, body {
    margin: 0;
    padding: 0;
    overflow: hidden;
    background: var(--sky);
  }
  .poster {
    display: block;
    width: 848px;
    height: 1200px;
  }
  .poster__sky { fill: var(--sky); }
  .poster__rays { fill: var(--ray); opacity: 0.35; }
  .band__fill { fill: var(--band); }
  .band__edge { stroke: var(--ink); stroke-width: 6; fill: none; }
  .tagline {
    font-family: "Poppins", sans-serif;
    font-weight: 500;
    font-size: 42px;
    fill: var(--ink);
  }
  .brand-name {
    font-family: "Poppins", sans-serif;
    font-weight: 800;
    font-size: 168px;
    fill: var(--ink);
  }
  .brand-dot { fill: var(--mark); }
  .asterisk { fill: var(--ink); }
</style>
</head>
<body>
<svg class="poster" viewBox="0 0 848 1200" xmlns="http://www.w3.org/2000/svg">
  <rect class="poster__sky" x="0" y="0" width="848" height="1200"/>

  <g class="poster__rays">
    <polygon points="848,1200 300,1200 420,1200"/>
    <polygon points="848,1200 520,1200 600,1140"/>
    <polygon points="848,1200 660,1010 720,980"/>
    <polygon points="848,1200 780,880 820,870"/>
    <polygon points="848,1200 848,760 848,820"/>
  </g>

  <g class="band">
    <polygon class="band__fill" points="0,782 565,0 848,0 848,396 283,1200 0,1200"/>
    <line class="band__edge" x1="0" y1="782" x2="565" y2="0"/>
    <line class="band__edge" x1="283" y1="1200" x2="848" y2="396"/>
  </g>

  <g class="band__content" transform="translate(424 600) rotate(-54)">
    <text class="tagline" x="-456" y="-112">Dine the wide-world style at</text>
    <text class="brand-name" x="-489" y="52" textLength="780" lengthAdjust="spacingAndGlyphs">BRONVEL</text>
    <circle class="brand-dot" cx="410" cy="-40" r="78"/>
  </g>

  <g class="asterisk" transform="translate(132 1074)">
    <rect x="-14" y="-56" width="28" height="112" rx="3"/>
    <rect x="-14" y="-56" width="28" height="112" rx="3" transform="rotate(60)"/>
    <rect x="-14" y="-56" width="28" height="112" rx="3" transform="rotate(120)"/>
  </g>
</svg>
</body>
</html>
```